Real Estate Company / Capital Needs Cards!

need business cards designed using the logos that were just designed by brightquill.

Target Market(s)

Investors and clients looking to purchase real estate or invest in the business.

Industry/Entity Type

Business

Requirements
Must have
• two designs - one for the real estate logo and one for the capital logo, similar but slightly different.
Nice to have
• something to make it pop (perhaps on the back)
Should not have
• much color

```html
<!DOCTYPE html>
<html lang="en">
<head>
<meta charset="utf-8">
<title>Merrow Real Estate — Business Cards</title>
<link href="https://fonts.googleapis.com/css2?family=Cinzel:wght@400;600&family=Open+Sans:wght@600&display=swap" rel="stylesheet">
<style>
  :root {
    --backdrop: #ecebe8;
    --card: #2b2d30;
    --card-edge: #222427;
    --silver: #e4e4e4;
    --silver-soft: #cfcfcf;
    --mark: #d9d9d9;
  }
  * { margin: 0; padding: 0; box-sizing: border-box; }
  html, body { width: 1200px; height: 498px; overflow: hidden; }
  body {
    background: var(--backdrop);
    display: flex;
    align-items: center;
    justify-content: center;
    gap: 40px;
    font-family: "Cinzel", serif;
  }
  .card {
    width: 540px;
    height: 300px;
    background: radial-gradient(ellipse at 50% 40%, #34363a 0%, var(--card) 60%, var(--card-edge) 100%);
    color: var(--silver);
    position: relative;
    display: flex;
    flex-direction: column;
    align-items: center;
    box-shadow: 0 2px 6px rgba(0,0,0,0.25);
  }

  /* Front */
  .card-front { padding-top: 46px; }
  .brand {
    display: flex;
    align-items: center;
    gap: 14px;
  }
  .brand-square {
    width: 56px;
    height: 56px;
    background: var(--mark);
    border-radius: 6px;
  }
  .brand-name {
    display: flex;
    flex-direction: column;
    font-weight: 400;
    color: var(--silver);
    line-height: 1;
  }
  .brand-name .primary { font-size: 42px; letter-spacing: 2px; }
  .brand-name .secondary { font-size: 17px; letter-spacing: 3px; margin-top: 4px; }

  .contact {
    margin-top: 42px;
    text-align: center;
    display: flex;
    flex-direction: column;
    align-items: center;
    gap: 6px;
    color: var(--silver-soft);
  }
  .contact .name-title { font-size: 19px; color: var(--silver); margin-bottom: 2px; }
  .contact .line { font-size: 15px; display: flex; align-items: center; gap: 6px; }
  .contact .line + .line { }
  .contact .address { font-size: 15px; margin-top: 4px; letter-spacing: 0.5px; }
  .icon { width: 13px; height: 13px; fill: var(--silver-soft); flex: none; }
  .pair { display: inline-flex; align-items: center; gap: 4px; }
  .pair + .pair { margin-left: 10px; }

  /* Back */
  .card-back { justify-content: center; }
  .back-square {
    position: absolute;
    width: 150px;
    height: 190px;
    left: 50%;
    top: 42px;
    transform: translateX(-50%);
    background: rgba(255,255,255,0.08);
    border-radius: 10px;
  }
  .back-name {
    position: relative;
    text-align: center;
    color: var(--silver);
    line-height: 1;
    margin-top: -24px;
  }
  .back-name .primary { display: block; font-size: 76px; letter-spacing: 3px; }
  .back-name .secondary { display: block; font-size: 30px; letter-spacing: 5px; margin-top: 4px; }
  .website {
    position: absolute;
    bottom: 34px;
    font-family: "Open Sans", sans-serif;
    font-weight: 600;
    font-size: 14px;
    letter-spacing: 3px;
    color: var(--silver);
  }
</style>
</head>
<body>

  <section class="card card-front">
    <div class="brand">
      <div class="brand-square"></div>
      <div class="brand-name">
        <span class="primary">MERROW</span>
        <span class="secondary">REAL ESTATE</span>
      </div>
    </div>

    <div class="contact">
      <p class="name-title">Your Name, Title</p>
      <p class="line">
        <span class="pair">
          <svg class="icon" viewBox="0 0 16 16" aria-hidden="true"><path d="M3.5 1.5l2.5 0 1.2 3.2-1.6 1.2a9 9 0 0 0 4.5 4.5l1.2-1.6 3.2 1.2v2.5c0 .8-.7 1.5-1.5 1.5A12.5 12.5 0 0 1 2 3c0-.8.7-1.5 1.5-1.5z"/></svg>
          123-456-7980
        </span>
        <span class="pair">
          <svg class="icon" viewBox="0 0 16 16" aria-hidden="true"><rect x="4" y="1" width="8" height="5"/><rect x="1" y="6" width="14" height="6" rx="1"/><rect x="4" y="10" width="8" height="5" fill="#2b2d30"/><rect x="5" y="11" width="6" height="3"/></svg>
          123-568-7896
        </span>
      </p>
      <p class="line">
        <svg class="icon" viewBox="0 0 16 16" aria-hidden="true"><rect x="1" y="3" width="14" height="10" rx="1"/><path d="M1.5 3.5L8 9l6.5-5.5" fill="none" stroke="#2b2d30" stroke-width="1.4"/></svg>
        hello@merrowrealestate.com
      </p>
      <p class="address">Street Name City Name State ZipCode</p>
    </div>
  </section>

  <section class="card card-back">
    <div class="back-square"></div>
    <div class="back-name">
      <span class="primary">MERROW</span>
      <span class="secondary">REAL ESTATE</span>
    </div>
    <p class="website">www.merrowrealestate.com</p>
  </section>

</body>
</html>
```